Bold Plum

I am starting a sharpening service for knives, scissors, and garden tools. It's a sole proprietorship, so it's a small business. The business name is "Bolt Plum." A one or two-page website is fine. Ember Guild has created a logo for me. There should be pictures of the things I sharpen. There will also be a price list for sharpened items. My address is: 18392 Calloway Lane, Stevenson Ranch, CA 91307. Phone number is 661-555-0172

```html
<!DOCTYPE html>
<html lang="en">
<head>
<meta charset="utf-8">
<title>Bolt Plum – Professional Sharpening</title>
<link href="https://fonts.googleapis.com/css2?family=Outfit:wght@400;500;600;700;800&family=Inter:wght@400;500&display=swap" rel="stylesheet">
<style>
:root{
  --blue:#2e5f86;
  --blue-dark:#244d6e;
  --orange:#e87b1e;
  --ink:#1d1d1f;
  --muted:#5c5c5c;
  --white:#ffffff;
  --wood:#5a4030;
}
*{box-sizing:border-box;margin:0;padding:0}
html,body{width:1200px;height:2821px;overflow:hidden;background:var(--white)}
body{position:relative;font-family:"Inter",Arial,sans-serif;color:var(--ink)}
.abs{position:absolute}
.heading{font-family:"Outfit",Arial,sans-serif}

/* header */
.top-rule{left:0;top:0;width:1200px;height:3px;background:var(--orange)}
.brand{font-family:"Outfit",Arial,sans-serif;font-weight:800;letter-spacing:1px;display:flex;align-items:center;gap:12px;white-space:nowrap}
.brand-dot{border-radius:50%;display:inline-block}
.header-brand{left:116px;top:40px;font-size:44px;color:var(--ink)}
.header-brand .brand-dot{width:26px;height:26px;background:var(--ink)}
.btn{display:flex;align-items:center;justify-content:center;border-radius:30px;color:var(--white);font-family:"Outfit",Arial,sans-serif;font-weight:600;text-transform:uppercase;white-space:nowrap}
.btn-blue{background:var(--blue)}
.btn-orange{background:var(--orange)}
.contact-btn{left:731px;top:25px;width:138px;height:43px;font-size:14px}
.phone-badge{left:895px;top:27px;width:41px;height:41px;border-radius:50%;background:var(--white);box-shadow:0 2px 8px rgba(0,0,0,.15);display:flex;align-items:center;justify-content:center}
.call-label{left:956px;top:26px;font-family:"Outfit",sans-serif;font-size:12.5px;color:var(--ink)}
.call-number{left:956px;top:42px;font-family:"Outfit",sans-serif;font-size:21px;font-weight:600;color:var(--blue)}
.main-nav{top:88px;left:0;font-family:"Outfit",sans-serif;font-size:16px;color:var(--ink)}
.main-nav a{position:absolute;color:inherit;text-decoration:none;white-space:nowrap}
.main-nav .active{color:var(--orange)}

/* hero */
.hero{left:0;top:132px;width:1200px;height:600px;
  background:
   radial-gradient(ellipse 260px 320px at 140px 170px,rgba(160,160,165,.55),transparent 70%),
   radial-gradient(ellipse 200px 330px at 1060px 280px,rgba(40,70,70,.6),transparent 70%),
   linear-gradient(160deg,#6a4c38 0%,#4e3727 45%,#3b2a1f 100%);
  clip-path:polygon(0 0,1200px 0,1200px 472px,600px 600px,0 472px)}
.hero-shade{left:0;top:132px;width:1200px;height:600px;background:rgba(20,12,8,.25);
  clip-path:polygon(0 0,1200px 0,1200px 472px,600px 600px,0 472px)}
.hero-brand{left:0;width:1200px;top:236px;justify-content:center;font-size:64px;color:var(--white)}
.hero-brand .brand-dot{width:36px;height:36px;background:var(--white)}
.hero-title{left:0;width:1200px;text-align:center;color:var(--white);font-family:"Outfit",sans-serif;font-weight:700;text-shadow:0 2px 10px rgba(0,0,0,.4)}
.hero-title.line1{top:398px;font-size:70px;letter-spacing:.5px}
.hero-title.line2{top:466px;font-size:53px}
.hero-sub{left:0;width:1200px;top:530px;text-align:center;color:var(--white);font-family:"Outfit",sans-serif;font-size:17.5px;line-height:27px}
.hero-btn{left:439px;top:599px;width:322px;height:46px;font-size:17px}
.hero-band{left:0;top:632px}

/* about */
.about-frame{left:125px;top:1007px;width:384px;height:395px;border:3px solid var(--orange);border-radius:36px}
.about-photo{left:162px;top:893px;width:421px;height:467px;border-radius:34px;border:4px solid var(--white);box-shadow:0 8px 24px rgba(0,0,0,.18);
  background:radial-gradient(ellipse 140px 120px at 300px 370px,#d48a3a,transparent 70%),linear-gradient(150deg,#3a2a1e,#6b4a32 50%,#2b1f17)}
.section-title{font-family:"Outfit",sans-serif;font-weight:700;color:var(--blue);text-transform:uppercase}
.section-title span{color:var(--orange)}
.about-title{left:681px;top:960px;width:420px;font-size:38px;line-height:42px}
.about-copy{left:681px;top:1057px;width:407px;font-size:15px;line-height:26.5px;color:var(--muted);text-align:justify}
.about-copy p+p{margin-top:26px}
.about-btn{left:681px;top:1318px;width:166px;height:42px;font-size:14px}

/* tools */
.tools-title{left:0;width:1200px;top:1556px;text-align:center;font-size:39px}
.tools-sub{left:0;width:1200px;top:1606px;text-align:center;font-family:"Outfit",sans-serif;font-size:19px;color:var(--ink)}
.tool-card{top:1661px;width:231px;height:359px;border:2px solid var(--blue);border-bottom-width:4px;border-radius:20px;background:var(--white)}
.tool-card.accent{border-color:var(--orange)}
.tool-photo{position:absolute;left:3px;top:3px;right:3px;height:172px;border-radius:16px 16px 0 0}
.tool-name{position:absolute;left:17px;top:192px;font-family:"Outfit",sans-serif;font-weight:600;font-size:16px;text-transform:uppercase}
.tool-kind{position:absolute;left:17px;top:214px;font-family:"Outfit",sans-serif;font-size:12.5px;color:var(--muted)}
.tool-price{position:absolute;right:17px;top:190px;font-family:"Outfit",sans-serif;font-weight:600;font-size:32px;color:var(--blue)}
.tool-rule{position:absolute;left:17px;right:17px;top:244px;border-top:1px dashed #9a9a9a}
.tool-desc{position:absolute;left:17px;right:17px;top:260px;font-size:12.5px;line-height:21px;color:var(--muted);text-align:justify}
.tool-btn{position:absolute;left:20px;bottom:-17px;width:124px;height:36px;font-size:12.5px}

/* call to action */
.footer-bg{left:0;top:0}
.cta-card{left:204px;top:2135px;width:792px;height:320px;border-radius:42px;border:4px solid var(--white);overflow:hidden;box-shadow:0 6px 20px rgba(0,0,0,.25);
  background:radial-gradient(ellipse 190px 150px at 150px 200px,rgba(205,120,40,.55),transparent 70%),linear-gradient(90deg,#3a2a1f 0%,#1b1a1a 45%,#121516 100%)}
.cta-title{left:567px;top:2256px;font-family:"Outfit",sans-serif;font-weight:700;font-size:39px;line-height:42px;color:var(--white)}
.cta-btn{left:567px;top:2357px;width:322px;height:47px;font-size:17px}

/* footer */
.footer-brand{left:112px;top:2538px;font-size:40px;color:var(--white)}
.footer-brand .brand-dot{width:24px;height:24px;background:var(--white)}
.footer-head{top:2521px;font-family:"Outfit",sans-serif;font-weight:600;font-size:21px;color:var(--white);text-transform:uppercase}
.footer-list{list-style:none;font-family:"Outfit",sans-serif;font-size:16px;color:var(--white)}
.footer-list li{position:relative;height:34.5px;display:flex;align-items:center;white-space:nowrap}
.footer-list .ico{position:absolute;left:-32px;top:11px;width:14px;height:14px}
.quick-links{left:462px;top:2553px}
.contact-list{left:702px;top:2553px}
.follow-list{left:1003px;top:2553px}
.footer-rule{left:112px;top:2760px;width:976px;border-top:1px dashed rgba(255,255,255,.55)}
.copyright{left:0;width:1200px;top:2784px;text-align:center;font-family:"Inter",sans-serif;font-size:13px;color:var(--white)}
</style>
</head>
<body>

<div class="abs top-rule"></div>

<header>
  <div class="abs brand header-brand"><span class="brand-dot"></span>BOLT PLUM</div>
  <a class="abs btn btn-blue contact-btn">Contact Us</a>
  <div class="abs phone-badge">
    <svg width="18" height="18" viewBox="0 0 24 24"><path fill="#2e5f86" d="M6.6 10.8a15.1 15.1 0 0 0 6.6 6.6l2.2-2.2a1 1 0 0 1 1-.25 11.4 11.4 0 0 0 3.6.57 1 1 0 0 1 1 1V20a1 1 0 0 1-1 1A17 17 0 0 1 3 4a1 1 0 0 1 1-1h3.5a1 1 0 0 1 1 1c0 1.25.2 2.45.57 3.6a1 1 0 0 1-.25 1z"/></svg>
  </div>
  <div class="abs call-label">Call to Book Sharpening</div>
  <div class="abs call-number">661-555-0172</div>
  <nav class="abs main-nav">
    <a class="active" style="left:529px">HOME</a>
    <a style="left:624px">About Bolt Plum</a>
    <a style="left:795px">Services</a>
    <a style="left:904px">Pricing</a>
    <a style="left:1003px">Testimonials</a>
  </nav>
</header>

<section class="hero-section">
  <div class="abs hero" role="img" aria-label="Chef knives, scissors and pruning shears laid out on a dark wooden workbench"></div>
  <div class="abs hero-shade"></div>
  <div class="abs brand hero-brand"><span class="brand-dot"></span>BOLT PLUM</div>
  <h1 class="abs hero-title line1">PROFESSIONAL</h1>
  <div class="abs hero-title line2">SHARPENING DONE RIGHT</div>
  <p class="abs hero-sub">Knives, scissors, and garden tools sharpened with precision -<br>fast turnaround and dependable service.</p>
  <a class="abs btn btn-orange hero-btn">Call to Book Sharpening</a>
  <svg class="abs hero-band" width="1200" height="130" viewBox="0 0 1200 130">
    <polygon points="112,3 112,22 600,126 1088,22 1088,3 600,105" fill="#2e5f86"/>
  </svg>
</section>

<section class="about">
  <div class="abs about-frame"></div>
  <div class="abs about-photo" role="img" aria-label="Craftsman in a hat and leather apron sharpening a blade on a grinding wheel with sparks"></div>
  <h2 class="abs section-title about-title">Sharp Tools. <span>Better Results.</span></h2>
  <div class="abs about-copy">
    <p>Bolt Plum is a local sharpening service dedicated to restoring edge performance for everyday tools. Whether it’s your kitchen knives, household scissors, or garden equipment, each item is sharpened with care and attention to detail. The goal is simple — give your tools a clean, durable edge that performs like new.</p>
    <p>As a small, owner-operated business, every job receives personal attention and professional handling.</p>
  </div>
  <a class="abs btn btn-blue about-btn">Explore More</a>
</section>

<section class="tools">
  <h2 class="abs section-title tools-title">Tools <span>We Service</span></h2>
  <p class="abs tools-sub">If it needs a sharp edge, we can likely restore it.</p>

  <article class="abs tool-card" style="left:112px">
    <div class="tool-photo" role="img" aria-label="Hands sharpening a kitchen knife on a whetstone" style="background:linear-gradient(160deg,#8c8f94,#3d4147 60%,#24272b)"></div>
    <div class="tool-name">Knives</div><div class="tool-kind">Kitchen Knives</div><div class="tool-price">$20</div>
    <div class="tool-rule"></div>
    <p class="tool-desc">Ut enim ad minima veniam, quis nostrum exercitationem ullam cor poris suscipit labor</p>
    <a class="btn btn-blue tool-btn">View Details</a>
  </article>

  <article class="abs tool-card accent" style="left:360px">
    <div class="tool-photo" role="img" aria-label="Hand holding a pair of household scissors" style="background:linear-gradient(160deg,#c9c3bc,#8a8078 55%,#5a514b)"></div>
    <div class="tool-name">Scissors</div><div class="tool-kind">Household Scissors</div><div class="tool-price">$20</div>
    <div class="tool-rule"></div>
    <p class="tool-desc">Ut enim ad minima veniam, quis nostrum exercitationem ullam cor poris suscipit labor</p>
    <a class="btn btn-orange tool-btn">View Details</a>
  </article>

  <article class="abs tool-card" style="left:609px">
    <div class="tool-photo" role="img" aria-label="Pruning shears cutting a leafy branch" style="background:linear-gradient(160deg,#4d6a36,#2e4222 55%,#1d2a16)"></div>
    <div class="tool-name">Garden Tools</div><div class="tool-kind">Garden shears</div><div class="tool-price">$20</div>
    <div class="tool-rule"></div>
    <p class="tool-desc">Ut enim ad minima veniam, quis nostrum exercitationem ullam cor poris suscipit labor</p>
    <a class="btn btn-blue tool-btn">View Details</a>
  </article>

  <article class="abs tool-card" style="left:857px">
    <div class="tool-photo" role="img" aria-label="Gloved hand trimming a hedge with an electric hedge trimmer" style="background:linear-gradient(160deg,#6d8a4a,#86a856 50%,#4f6d32)"></div>
    <div class="tool-name">Others</div><div class="tool-kind">Utility blades</div><div class="tool-price">$20</div>
    <div class="tool-rule"></div>
    <p class="tool-desc">Ut enim ad minima veniam, quis nostrum exercitationem ullam cor poris suscipit labor</p>
    <a class="btn btn-blue tool-btn">View Details</a>
  </article>
</section>

<svg class="abs footer-bg" width="1200" height="2821" viewBox="0 0 1200 2821">
  <polygon points="0,2388 600,2270 1200,2388 1200,2821 0,2821" fill="#2e5f86"/>
  <polygon points="112,2330 204,2305 204,2340 112,2368" fill="#e87b1e"/>
  <polygon points="996,2305 1088,2330 1088,2368 996,2340" fill="#e87b1e"/>
</svg>

<section class="cta">
  <div class="abs cta-card" role="img" aria-label="Angle grinder cutting metal with a shower of sparks in a dark workshop"></div>
  <h2 class="abs cta-title">BRING YOUR TOOLS<br>BACK TO LIFE</h2>
  <a class="abs btn btn-orange cta-btn">Call to Book Sharpening</a>
</section>

<footer>
  <div class="abs brand footer-brand"><span class="brand-dot"></span>BOLT PLUM</div>

  <h3 class="abs footer-head" style="left:430px">Quick Links</h3>
  <ul class="abs footer-list quick-links">
    <li><svg class="ico" viewBox="0 0 14 14"><path d="M3 3l4 4-4 4M7 3l4 4-4 4" stroke="#fff" stroke-width="1.6" fill="none"/></svg>Home</li>
    <li><svg class="ico" viewBox="0 0 14 14"><path d="M3 3l4 4-4 4M7 3l4 4-4 4" stroke="#fff" stroke-width="1.6" fill="none"/></svg>About Us</li>
    <li><svg class="ico" viewBox="0 0 14 14"><path d="M3 3l4 4-4 4M7 3l4 4-4 4" stroke="#fff" stroke-width="1.6" fill="none"/></svg>Services / Pricing</li>
    <li><svg class="ico" viewBox="0 0 14 14"><path d="M3 3l4 4-4 4M7 3l4 4-4 4" stroke="#fff" stroke-width="1.6" fill="none"/></svg>Testimonials</li>
    <li><svg class="ico" viewBox="0 0 14 14"><path d="M3 3l4 4-4 4M7 3l4 4-4 4" stroke="#fff" stroke-width="1.6" fill="none"/></svg>Contact Us</li>
  </ul>

  <h3 class="abs footer-head" style="left:671px">Contact Us</h3>
  <ul class="abs footer-list contact-list">
    <li><svg class="ico" viewBox="0 0 14 14"><path d="M7 1a4 4 0 0 0-4 4c0 3 4 8 4 8s4-5 4-8a4 4 0 0 0-4-4zm0 5.5A1.5 1.5 0 1 1 7 3.5a1.5 1.5 0 0 1 0 3z" fill="#fff"/></svg>18392 Calloway Lane,</li>
    <li>Stevenson Ranch, CA 91307</li>
    <li><svg class="ico" viewBox="0 0 24 24"><path fill="#fff" d="M6.6 10.8a15.1 15.1 0 0 0 6.6 6.6l2.2-2.2a1 1 0 0 1 1-.25 11.4 11.4 0 0 0 3.6.57 1 1 0 0 1 1 1V20a1 1 0 0 1-1 1A17 17 0 0 1 3 4a1 1 0 0 1 1-1h3.5a1 1 0 0 1 1 1c0 1.25.2 2.45.57 3.6a1 1 0 0 1-.25 1z"/></svg>661-555-0172</li>
    <li><svg class="ico" viewBox="0 0 14 14"><rect x="1" y="3" width="12" height="8" rx="1" fill="#fff"/><path d="M1.5 3.5L7 8l5.5-4.5" stroke="#2e5f86" stroke-width="1.2" fill="none"/></svg>info@boltplum.com</li>
  </ul>

  <h3 class="abs footer-head" style="left:971px">Follow Us</h3>
  <ul class="abs footer-list follow-list">
    <li><svg class="ico" viewBox="0 0 14 14"><rect x="1" y="1" width="12" height="12" rx="2" fill="#fff"/></svg>Friendpage</li>
    <li><svg class="ico" viewBox="0 0 14 14"><rect x="1" y="1" width="12" height="12" rx="2" fill="#fff"/></svg>Snapgram</li>
    <li><svg class="ico" viewBox="0 0 14 14"><rect x="1" y="1" width="12" height="12" rx="2" fill="#fff"/></svg>Viewtube</li>
  </ul>

  <div class="abs footer-rule"></div>
  <p class="abs copyright">(C) Copyright 2026 | All Rights Reserved</p>
</footer>

</body>
</html>
```